Corvanta512 Business Card Redesign

I want to create a design for brand new business cards, I need something exceptional for clear plastic business card design. Please do not submit without it being on a clear design. Photos of the various logo versions attached.

```html
<!DOCTYPE html>
<html lang="en">
<head>
<meta charset="utf-8">
<title>Corvanta512 Business Card</title>
<link href="https://fonts.googleapis.com/css2?family=Jost:wght@300;400;600&display=swap" rel="stylesheet">
<style>
  :root {
    --backdrop: #1b1b1c;
    --card-top: #9a9c9e;
    --card-bottom: #828486;
    --card-edge: rgba(255,255,255,0.35);
    --ink-light: #f4f5f6;
    --ink-soft: #e3e4e6;
    --brand-gold: #d2b46c;
    --brand-navy: #2c3e63;
    --deco-light: rgba(255,255,255,0.75);
  }
  * { margin: 0; padding: 0; box-sizing: border-box; }
  html, body { width: 1200px; height: 800px; overflow: hidden; }
  body {
    background: var(--backdrop);
    font-family: "Jost", sans-serif;
    display: flex;
    align-items: center;
    justify-content: center;
  }
  .business-card {
    position: relative;
    width: 1000px;
    height: 580px;
    border-radius: 36px;
    background: linear-gradient(160deg, var(--card-top), var(--card-bottom));
    border: 2px solid var(--card-edge);
    overflow: hidden;
  }
  .decor-area {
    position: absolute;
    left: 0;
    top: 40px;
    width: 360px;
    height: 260px;
    border-radius: 0 0 200px 0;
    background: radial-gradient(ellipse at 30% 30%, var(--deco-light), rgba(255,255,255,0.15) 70%, transparent);
  }
  .brand {
    position: absolute;
    right: 90px;
    top: 120px;
    display: flex;
    align-items: center;
    gap: 16px;
  }
  .brand-dot {
    width: 34px;
    height: 34px;
    border-radius: 50%;
    background: var(--brand-navy);
  }
  .brand-name {
    font-weight: 600;
    font-size: 56px;
    letter-spacing: 1px;
    color: var(--brand-gold);
  }
  .person {
    position: absolute;
    right: 400px;
    top: 315px;
    text-align: right;
    color: var(--ink-light);
    white-space: nowrap;
  }
  .person-name {
    font-size: 56px;
    letter-spacing: 3px;
    line-height: 1;
    text-transform: uppercase;
  }
  .person-name .first { font-weight: 300; }
  .person-name .last { font-weight: 600; }
  .person-role {
    font-weight: 300;
    font-size: 20px;
    color: var(--ink-soft);
    margin-top: 6px;
  }
  .divider {
    position: absolute;
    left: 624px;
    top: 395px;
    width: 2px;
    height: 110px;
    background: var(--ink-soft);
  }
  .contact {
    position: absolute;
    right: 60px;
    top: 410px;
    list-style: none;
    color: var(--ink-light);
    font-size: 22px;
    font-weight: 300;
    line-height: 1.36;
  }
  .contact li { display: flex; justify-content: flex-end; gap: 18px; }
  .contact .label { width: 16px; font-weight: 600; }
  .contact .web { font-weight: 600; }
</style>
</head>
<body>
  <div class="business-card">
    <div class="decor-area" role="img" aria-label="Soft frosted decorative area"></div>

    <div class="brand">
      <span class="brand-dot"></span>
      <span class="brand-name">Corvanta512</span>
    </div>

    <div class="person">
      <p class="person-name"><span class="first">Mateo</span> <span class="last">Varga</span></p>
      <p class="person-role">UI &amp; UX designer</p>
    </div>

    <div class="divider"></div>

    <ul class="contact">
      <li><span>Serving clients nationwide</span><span class="label"></span></li>
      <li><span>1-800-555-0142</span><span class="label">T</span></li>
      <li><span>info@corvanta512.com</span><span class="label">E</span></li>
      <li><span class="web">corvanta512.com</span><span class="label"></span></li>
    </ul>
  </div>
</body>
</html>
```